Cover Photo Design Needed for Business

We need a Facebook cover photo design for a new company called "Quillmarestan". Our goal is to enable your success through the free exchange of wisdom and tools through other entrepreneur's. For those looking to take further steps, we offer several paid services that can help you start, manage, and grow your venture. Were looking for something new and creative.

Industry/Entity Type

Business

Requirements
Nice to have
• If it goes with the cover photo we would like an arrow pointing to the like button.

```html
<!DOCTYPE html>
<html lang="en">
<head>
<meta charset="utf-8">
<title>Quillmarestan – Cover</title>
<link rel="stylesheet" href="https://fonts.googleapis.com/css2?family=Cabin:wght@400&display=swap">
<style>
  :root {
    --bg-green: #9dc300;
    --mark-grey: #6e706c;
    --arrow-light: #8a8c88;
    --arrow-dark: #5c5e5a;
    --word-white: #ffffff;
    --like-blue: #0000ff;
  }
  html, body {
    margin: 0;
    padding: 0;
    overflow: hidden;
    background: var(--bg-green);
  }
  .cover {
    position: relative;
    width: 1200px;
    height: 444px;
    background: var(--bg-green);
    overflow: hidden;
    font-family: "Cabin", "Gill Sans", sans-serif;
  }
  .brand-mark {
    position: absolute;
    left: 78px;
    top: 33px;
    width: 380px;
    height: 380px;
    border-radius: 50%;
    background: var(--mark-grey);
  }
  .brand-name {
    position: absolute;
    left: 462px;
    top: 118px;
    margin: 0;
    font-size: 88px;
    font-weight: 400;
    line-height: 1;
    letter-spacing: -0.5px;
    color: var(--word-white);
  }
  .like-pointer {
    position: absolute;
    left: 890px;
    top: 255px;
    width: 90px;
    height: 172px;
  }
  .like-label {
    position: absolute;
    left: 991px;
    top: 317px;
    font-size: 40px;
    line-height: 1;
    color: var(--like-blue);
  }
</style>
</head>
<body>
  <main class="cover">
    <div class="brand-mark" aria-hidden="true"></div>
    <h1 class="brand-name">Quillmarestan</h1>

    <svg class="like-pointer" viewBox="0 0 90 172" aria-hidden="true">
      <defs>
        <linearGradient id="pointer-shade" x1="0" y1="0" x2="1" y2="0">
          <stop offset="0" stop-color="var(--arrow-dark)"/>
          <stop offset="0.45" stop-color="var(--arrow-light)"/>
          <stop offset="1" stop-color="var(--arrow-dark)"/>
        </linearGradient>
      </defs>
      <path d="M26 6 Q26 2 30 2 L54 2 Q58 2 58 6 L58 72 L83 72 Q88 72 85 78 L50 166 Q46 172 42 166 L6 80 Q3 72 9 72 L26 72 Z"
            fill="url(#pointer-shade)"/>
    </svg>
    <span class="like-label">Like</span>
  </main>
</body>
</html>
```